PowerPoint presentation

Please clean up this presentation using the overall look of Brovane's brand. www.brovanereit.com. Looking for clean, contemporary, easy to read.

This presentation will be sent to customers to educate them about resources available to them for cost and energy savings.

```html
<!DOCTYPE html>
<html lang="en">
<head>
<meta charset="utf-8">
<title>Brovane E-Playbook – Slide Overview</title>
<link href="https://fonts.googleapis.com/css2?family=Montserrat:wght@300;400;600;700;800&family=Source+Sans+3:wght@400;600;700&display=swap" rel="stylesheet">
<style>
:root{
  --page:#a4a4a4;
  --navy:#0b2d82;
  --navy-deep:#0a1f5e;
  --blue:#1a56c4;
  --mid:#1f6fd0;
  --sky:#5aa0dc;
  --light:#7cc3e8;
  --pale:#cfe7f6;
  --ink:#1b1b2a;
  --white:#ffffff;
}
*{box-sizing:border-box;margin:0;padding:0}
html,body{width:1200px;height:640px;overflow:hidden}
body{background:var(--page);font-family:"Source Sans 3",sans-serif;color:var(--ink);position:relative}
.slide{position:absolute;width:356px;height:267px;background:var(--white);overflow:hidden;box-shadow:0 6px 14px rgba(0,0,0,.22)}
.col-1{left:40px}.col-2{left:422px}.col-3{left:805px}
.row-1{top:40px}.row-2{top:333px}
.abs{position:absolute}
.title-bar{position:absolute;left:0;top:18px;height:21px;background:var(--navy);color:var(--white);font:800 14.5px/21px "Montserrat",sans-serif;padding-left:21px;letter-spacing:.6px;clip-path:polygon(0 0,calc(100% - 8px) 0,100% 50%,calc(100% - 8px) 100%,0 100%)}
.lead{position:absolute;left:21px;color:var(--blue);font:400 11px/14px "Source Sans 3",sans-serif}
.bullets{list-style:none;color:var(--white)}
.bullets li{position:relative;padding-left:7px}
.bullets li::before{content:"";position:absolute;left:0;top:.45em;width:3px;height:3px;background:var(--light);transform:rotate(45deg)}
.bullets b{font-weight:700}
.photo{position:absolute}

/* cover */
.cover-mark{position:absolute;left:22px;top:34px;display:flex;align-items:center;gap:8px}
.cover-mark .sq{width:28px;height:28px;background:var(--navy)}
.cover-mark .name{font:800 24px "Montserrat",sans-serif;color:var(--navy)}
.cover-draft{left:14px;top:193px;font:400 11px "Source Sans 3",sans-serif}
.cover-bar{position:absolute;left:0;top:209px;width:162px;height:28px;background:var(--navy);color:var(--white);font:800 18px/28px "Montserrat",sans-serif;padding-left:15px;letter-spacing:.5px;clip-path:polygon(0 0,calc(100% - 10px) 0,100% 50%,calc(100% - 10px) 100%,0 100%)}
.cover-art{right:0;top:0;width:200px;height:267px;background:linear-gradient(120deg,var(--white) 0%,var(--pale) 30%,var(--light) 60%,var(--mid) 85%,var(--navy) 100%);clip-path:polygon(45% 0,100% 0,100% 100%,45% 100%,0 50%)}

/* purpose slide */
.purpose-body{left:21px;top:77px;width:320px;font:400 6.8px/9.4px "Source Sans 3",sans-serif}
.purpose-band{left:0;top:108px;width:178px;height:159px;background:var(--navy)}
.purpose-list{left:18px;top:126px;width:152px;font:400 5.2px/7px "Source Sans 3",sans-serif}
.purpose-list li{margin-bottom:4.6px}

/* team slide */
.team-band{left:0;top:95px;width:356px;height:172px;background:var(--navy)}
.team-list{left:20px;top:107px;width:270px;font:400 4.6px/6px "Source Sans 3",sans-serif}
.team-list>li{margin-bottom:3px}
.team-list ul{list-style:none;margin-top:2px}
.team-list ul li{position:relative;padding-left:5px;margin-bottom:2.6px;font-size:4.1px;line-height:5.4px}
.team-list ul li::before{content:"";position:absolute;left:0;top:1.6px;border-left:2.6px solid var(--light);border-top:1.5px solid transparent;border-bottom:1.5px solid transparent}

/* vendor slide */
.vendor-grid{position:absolute;left:20px;top:73px;display:grid;grid-template-columns:repeat(5,59px);grid-auto-rows:32px;gap:3.6px 5px}
.vendor{border:1px solid #d3d7df;display:flex;align-items:center;justify-content:center;gap:3px;font:700 7.2px "Source Sans 3",sans-serif;color:var(--navy);text-align:center;line-height:8px;padding:0 3px}
.vendor .dot{width:5px;height:5px;border-radius:50%;background:var(--navy);flex:none}

/* multi-level */
.ml-sub{left:21px;top:78px;font:400 7.5px/9.6px "Source Sans 3",sans-serif;color:var(--ink)}
.level-desc{position:absolute;color:var(--white);font:400 5.3px/7.4px "Source Sans 3",sans-serif}
.level-desc b{font-weight:700}

/* 80/20 */
.rule-left{left:0;top:66px;width:178px;height:201px;background:var(--navy)}
.rule-right{left:178px;top:66px;width:178px;height:201px;background:var(--navy-deep)}
.rule-text{left:20px;top:82px;width:150px;color:var(--white);font:400 5px/6.4px "Source Sans 3",sans-serif}
.rule-text h4{font:700 5.4px/6.6px "Source Sans 3",sans-serif;margin-bottom:1px}
.rule-text .bullets li{margin-bottom:2px}
.rule-text .bullets li::before{top:2px;width:2.6px;height:2.6px}
.chart-title{position:absolute;color:var(--white);font:700 5.6px "Source Sans 3",sans-serif;width:178px;text-align:center;left:178px}
.pie{position:absolute;border-radius:50%}
.pie-1{left:234px;top:92px;width:64px;height:64px;background:conic-gradient(#5aa8e0 0 18%,#0d3d9c 18% 19%,#3d7fd2 19% 37%,#6fb5e6 37% 52%,#1b4fae 52% 57%,#173e93 57% 77%,#2c66c3 77% 79%,#82c3ec 79% 88%,#4a8fdb 88% 97%,#214e9f 97% 100%)}
.pie-1::after{content:"";position:absolute;left:24px;top:24px;width:16px;height:16px;border-radius:50%;background:var(--navy-deep)}
.pie-2{left:232px;top:174px;width:60px;height:60px;background:conic-gradient(#6fb5e6 0 46%,#4a8fdb 46% 48%,#173e93 48% 94%,#2c66c3 94% 100%)}
.pie-2::after{content:"";position:absolute;left:22px;top:22px;width:16px;height:16px;border-radius:50%;background:var(--navy-deep)}
.chart-label{position:absolute;color:var(--white);font:400 3.9px "Source Sans 3",sans-serif;border-bottom:.5px solid rgba(255,255,255,.6);padding-bottom:1px;width:50px}
.chart-label.l{left:196px}
.chart-label.r{right:8px;text-align:right}
.rule-foot{left:211px;top:248px;display:flex;align-items:center;gap:6px;color:var(--white)}
.rule-foot .sq{width:5px;height:5px;background:var(--white)}
.rule-foot .brand{font:700 5px "Source Sans 3",sans-serif;width:40px}
.rule-foot .cap{font:700 4.2px/5px "Montserrat",sans-serif;width:80px}
</style>
</head>
<body>

<!-- Cover -->
<section class="slide col-1 row-1">
  <div class="photo cover-art" role="img" aria-label="Decorative blue diagonal stripe graphic"></div>
  <div class="cover-mark"><span class="sq"></span><span class="name">Brovane</span></div>
  <p class="abs cover-draft">DRAFT 2.7.25</p>
  <div class="cover-bar">E-PLAYBOOK</div>
</section>

<!-- The E-Playbook -->
<section class="slide col-2 row-1">
  <div class="title-bar" style="width:188px">THE E-PLAYBOOK</div>
  <p class="lead" style="top:44px;width:320px">Purpose is to operationalize Brovane's commitment to supporting our tenant operators' efficient and sustainable practices.</p>
  <p class="abs purpose-body">Working with our Operators, Third-Party Advisors, and Preferred Vendors, Brovane has established consistent and comprehensive practices and approaches that can be replicated and scaled, including:</p>
  <div class="abs purpose-band"></div>
  <div class="photo" role="img" aria-label="Photo of hands holding a small plant growing inside a globe frame" style="left:178px;top:108px;width:178px;height:159px;background:linear-gradient(135deg,#7cc8ec,#5cb4e2)"></div>
  <ul class="bullets abs purpose-list">
    <li>Practical and holistic whole-building approach to energy and water efficiency opportunities.</li>
    <li>Knowledgeable and vetted third-party advisors and vendors with technical expertise and proven experience in the senior living and care space, REIT structure, and Brovane.</li>
    <li>Responsive and collaborative services from upfront advice to project assessment and solutions to project support and management.</li>
    <li>Best practices, including established and innovative new technologies, implemented successfully across other senior living and care properties and organizations.</li>
    <li>Access to rebates, incentives, and financing from Brovane and other third parties.</li>
    <li>Awareness and support around evolving benchmarking and other regulatory compliance.</li>
  </ul>
</section>

<!-- Team -->
<section class="slide col-3 row-1">
  <div class="title-bar" style="width:216px">E-PLAYBOOK TEAM</div>
  <p class="lead" style="top:44px;width:320px;line-height:13.4px">Brovane provides a collaborative team that knows the opportunities and challenges of efficient and sustainable practices as well as the nuances of senior living and care</p>
  <div class="abs team-band"></div>
  <div class="photo" role="img" aria-label="Overhead photo of a team working together at a table" style="left:294px;top:95px;width:62px;height:172px;background:linear-gradient(160deg,#e9e4dc,#c9c3bb 55%,#8f9aa8)"></div>
  <ul class="bullets abs team-list">
    <li><b>Brovane Management:</b> Sustainability (Jana Pruitt), Facilities and Capital Projects (Owen Hale), Asset Management (Lena Marsh)</li>
    <li><b>Program Advisor:</b> Hollyfield E-Advisory (Neil Barrow), over 30 years of senior real estate expertise, providing a broad range of sustainability practices, leadership, and access to a preferred vendor network, including technical advisors</li>
    <li><b>Technical Advisors:</b> trusted and seasoned advisors with engagement and domain expertise across the prop-tech, health-tech, benchmarking, and renewable sectors of senior living and care
      <ul>
        <li><b>Clearfield E-3 Partners:</b> (Rick Dorsey and Paul Wexler), providing ongoing advice and consultation to owners and operators. Helped implement over $3.5 million of Lighting, Water, and HVAC projects for Healthcare REITs over the last two years.</li>
        <li><b>Bellavita Health Advisory Services:</b> (Maria Renn), former Chief Clinical Officer at Daybreak Senior Living, 30-year experience improving quality and business results through strategic planning, innovation, and application of health-tech solutions, including fall management and continuous vital sign monitoring.</li>
        <li><b>Verdelo:</b> (Ilona Varga), team includes Certified Energy Auditors (CEA), Certified Energy Managers (CEM), and energy and water Data Analysts. They provide utility collection, verification, ESPM integration, Benchmarking, and energy audits for owners and operators.</li>
        <li><b>SunLedger:</b> (Dana Crewe), former CFO/CPA with 20 years of real estate and solar experience, helping owners and operators evaluate the pros and cons of solar applications.</li>
      </ul>
    </li>
    <li><b>Preferred Vendors:</b> over 25 preferred and vetted vendors actively engaged and providing services across the senior living and care sector, ranging from energy and water efficiency to utility rebates and financing to rooftop and community solar</li>
  </ul>
</section>

<!-- Vendors -->
<section class="slide col-1 row-2">
  <div class="title-bar" style="width:202px">REPRESENTATIVE</div>
  <p class="lead" style="top:44px">PREFERRED VENDORS</p>
  <div class="vendor-grid">
    <div class="vendor"><span class="dot"></span>Skyguard</div>
    <div class="vendor">Coolmark</div>
    <div class="vendor">Voltara</div>
    <div class="vendor">Dropwise</div>
    <div class="vendor">Clearfield</div>
    <div class="vendor">Arcway Renewables</div>
    <div class="vendor">Meterline</div>
    <div class="vendor">Thermacore</div>
    <div class="vendor">AirAudit</div>
    <div class="vendor">Careway Supply</div>
    <div class="vendor">Flowkeep</div>
    <div class="vendor">Verdelo</div>
    <div class="vendor">Rainlogic</div>
    <div class="vendor">Watchwell</div>
    <div class="vendor">Norvest Fund</div>
    <div class="vendor">Gridline</div>
    <div class="vendor">Summit HVAC</div>
    <div class="vendor"><span class="dot"></span>Carelens</div>
    <div class="vendor">Coolbreeze Intl</div>
    <div class="vendor">SunLedger</div>
    <div class="vendor">Tempo</div>
    <div class="vendor">Fernleaf Capital</div>
    <div class="vendor">Habitat Cube</div>
    <div class="vendor">Living Lab Co</div>
    <div class="vendor"><span class="dot"></span>Pulsewave</div>
  </div>
</section>

<!-- Multi-level -->
<section class="slide col-2 row-2">
  <div class="title-bar" style="width:165px">MULTI-LEVEL</div>
  <p class="lead" style="top:44px;line-height:13.6px">APPROACH TO<br>BUILDING EFFICIENCY</p>
  <p class="abs ml-sub">ENERGY AND WATER<br>SAVINGS POTENTIAL</p>
  <svg class="abs" style="left:0;top:0" width="356" height="267" viewBox="0 0 356 267">
    <defs>
      <linearGradient id="rise" x1="0" y1="1" x2="1" y2="0">
        <stop offset="0" stop-color="#cfe7f6"/>
        <stop offset="1" stop-color="#3f8fd6"/>
      </linearGradient>
    </defs>
    <polygon points="12,241 200,62 193,55 228,52 223,87 216,80 28,259" fill="url(#rise)"/>
    <polygon points="42,227 356,227 356,267 2,267" fill="#7cc3e8"/>
    <polygon points="92,186 356,186 356,225 53,225" fill="#5aa0dc"/>
    <polygon points="136,151 356,151 356,184 103,184" fill="#1f6fd0"/>
    <polygon points="176,115 356,115 356,148 143,148" fill="#1452b0"/>
    <polygon points="220,84 356,84 356,114 190,114" fill="#0b2d82"/>
    <g font-family="Montserrat,sans-serif" font-weight="800" font-size="7" fill="#fff">
      <text transform="translate(207,112) rotate(-60)">LEVEL</text>
      <text transform="translate(166,147) rotate(-60)">LEVEL</text>
      <text transform="translate(125,182) rotate(-60)">LEVEL</text>
      <text transform="translate(83,223) rotate(-60)">LEVEL</text>
      <text transform="translate(41,263) rotate(-60)">LEVEL</text>
    </g>
    <g font-family="Montserrat,sans-serif" font-weight="300" font-size="23" fill="none" stroke="#fff" stroke-width=".7">
      <text x="229" y="110">05</text>
      <text x="198" y="145">04</text>
      <text x="156" y="181">03</text>
      <text x="111" y="221">02</text>
      <text x="69" y="263">01</text>
    </g>
    <g fill="#1a56c4" stroke="#fff" stroke-width="1">
      <circle cx="183" cy="99" r="11"/>
      <circle cx="145" cy="132" r="11"/>
      <circle cx="106" cy="166" r="11"/>
      <circle cx="59" cy="205" r="11"/>
      <circle cx="14" cy="246" r="11"/>
    </g>
    <g font-family="Montserrat,sans-serif" font-weight="700" font-size="6" fill="#fff" text-anchor="middle">
      <text x="183" y="101">50%</text>
      <text x="145" y="134">40%</text>
      <text x="106" y="168">30%</text>
      <text x="59" y="207">20%</text>
      <text x="14" y="248">10%</text>
    </g>
  </svg>
  <p class="level-desc" style="left:263px;top:87px;width:90px"><b>Smart</b> whole building strategy including Solar, Battery Storage and EV charging stations</p>
  <p class="level-desc" style="left:233px;top:122px;width:118px"><b>Efficient</b> capital replacement strategy including HVAC, Mechanicals, Building Envelope and Roofing</p>
  <p class="level-desc" style="left:189px;top:159px;width:162px"><b>Enhanced</b> HVAC maintenance, insulation, and efficiency technology such as Smart Thermostats, Smart Motors and Chips</p>
  <p class="level-desc" style="left:148px;top:198px;width:200px"><b>Practical</b> whole building technology such as Water Efficiency Valves and Power Grid Filters</p>
  <p class="level-desc" style="left:100px;top:240px;width:250px"><b>Initial</b> LED lighting and Water Efficiency Improvements such as low flow plumbing fixtures, smart irrigation &amp; landscape</p>
</section>

<!-- 80/20 -->
<section class="slide col-3 row-2">
  <div class="title-bar" style="width:216px">E-PLAYBOOK - 80/20</div>
  <p class="lead" style="top:44px">Energy Efficiency Rule</p>
  <div class="abs rule-left"></div>
  <div class="abs rule-right"></div>
  <div class="abs rule-text">
    <h4>In Senior Living &amp; Care, HVAC, Lighting, and Water Heating typically accounts for up to 80% of energy use*:</h4>
    <ul class="bullets">
      <li>Electricity uses include: 18% lighting, 1% water heating, 18% ventilation, 15% space cooling, 5% space heating, 20% miscellaneous, 2% computing, 9% office equipment, 9% refrigeration, and 3% cooking.</li>
      <li>Natural gas uses include: 46% water heating, 46% space heating, 2% miscellaneous, and 6% cooking.</li>
    </ul>
    <h4 style="margin-top:6px">HVAC Lesson Learned:</h4>
    <ul class="bullets">
      <li>Single largest equipment investment at most properties, often over $1million+</li>
      <li>Up to 60% of total energy cost</li>
      <li>It is not just the upfront or replacement cost but the total cost of ownership, including maintenance, preservation, and efficiency</li>
      <li>Proper maintenance is a critical component to overall efficiency, preservation, and ownership cost</li>
      <li>You need to stay on top of issues and plan ahead</li>
      <li>If you make a mistake, you will have to live with it for the next 15 years (less if you don't maintain it)</li>
      <li>Operators need to be both Care and Real Estate focused</li>
    </ul>
  </div>
  <p class="chart-title" style="top:78px">Electricity End Uses</p>
  <div class="pie pie-1" role="img" aria-label="Pie chart of electricity end uses"></div>
  <span class="chart-label l" style="top:84px">20% Miscellaneous</span>
  <span class="chart-label l" style="top:100px">02% Computing</span>
  <span class="chart-label l" style="top:116px">09% Office Equipment</span>
  <span class="chart-label l" style="top:132px">09% Refrigeration</span>
  <span class="chart-label l" style="top:148px">03% Cooking</span>
  <span class="chart-label r" style="top:84px">Space Heating 05%</span>
  <span class="chart-label r" style="top:100px">Space Cooling 15%</span>
  <span class="chart-label r" style="top:116px">Ventilation 18%</span>
  <span class="chart-label r" style="top:132px">Water Heating 1%</span>
  <span class="chart-label r" style="top:148px">Lighting 18%</span>
  <p class="chart-title" style="top:164px">Electricity End Uses</p>
  <div class="pie pie-2" role="img" aria-label="Pie chart of natural gas end uses"></div>
  <span class="chart-label l" style="top:187px">06% Cooking</span>
  <span class="chart-label l" style="top:219px">46% Water Heating</span>
  <span class="chart-label r" style="top:187px">Miscellaneous 2%</span>
  <span class="chart-label r" style="top:219px">Space Heating 46%</span>
  <div class="abs rule-foot">
    <span class="sq"></span>
    <span class="brand">Prairieland Energy</span>
    <span class="cap">AVERAGE EUI FOR NURSING HOMES IN THE MIDWEST</span>
  </div>
</section>

</body>
</html>
```